QVAR Individual and Corporate Development Business Card Design

QVAR needs a business card design that is aligned with it's values and targetted markets. Harmonic Lattice of Cognition Network's self diagnosis model and tools, which can be used for personal improvement and team/business performance enhancement, is based on the learnings of over 20 years of medical practitioning. QVAR supercharges personal effectiveness and awareness to also increase team and business performance.

The targetted markets are high performance individuals and teams who aspire seek to enhance their capabilities and achieve their absolute best potential.

Look and feel for the business card design we are looking for is high technology, premium, fresh, new and medical.

Target Market(s)

Industry/Entity Type

Business Consultant

Contact Information for Business Card

Logo, Full Name, Title, Phone number, Email, company name, Address,

Font styles to use
Sans Serif

Requirements
Must have
• Tag line: Maximising Performance for Highly Effective People
• Please use same colours as the logo.

```html
<!DOCTYPE html>
<html lang="en">
<head>
<meta charset="utf-8">
<title>QVAR Business Card</title>
<link rel="stylesheet" href="https://fonts.googleapis.com/css2?family=Exo+2:wght@500;700&family=Roboto:wght@400&display=swap">
<style>
  :root {
    --teal: #00a6bf;
    --slate: #5a5f65;
    --mist: #a9adb1;
    --ink: #0c0c0d;
    --paper: #ffffff;
    --backdrop: #3a3b3d;
  }
  * { margin: 0; padding: 0; box-sizing: border-box; }
  html, body { width: 1200px; height: 900px; overflow: hidden; }
  body {
    background: var(--backdrop);
    display: flex;
    flex-direction: column;
    align-items: center;
    justify-content: center;
    gap: 40px;
    font-family: "Roboto", Arial, sans-serif;
  }
  .card {
    position: relative;
    width: 700px;
    height: 400px;
    border-radius: 22px;
    overflow: hidden;
  }
  .card--back { background: var(--ink); }
  .card--front { background: var(--paper); }

  .lockup {
    position: absolute;
    display: flex;
    flex-direction: column;
    align-items: flex-start;
    font-family: "Exo 2", Arial, sans-serif;
    font-weight: 700;
    color: var(--teal);
  }
  .lockup__row { display: flex; align-items: center; gap: 14px; }
  .lockup__mark { width: 16px; height: 16px; background: var(--teal); }
  .lockup__name { font-size: 78px; line-height: 1; letter-spacing: 4px; }
  .lockup__rule { width: 100%; height: 2px; background: var(--mist); margin: 18px 0 8px; }
  .lockup__full { font-size: 17px; letter-spacing: 1.5px; line-height: 1.15; text-transform: uppercase; }

  .card--back .lockup { left: 50%; top: 46%; transform: translate(-50%, -50%); }
  .card--front .lockup { left: 50%; top: 24px; transform: translateX(-40%); }

  .tagline {
    position: absolute;
    left: 0; right: 0; bottom: 34px;
    text-align: center;
    font-family: "Exo 2", Arial, sans-serif;
    font-weight: 500;
    font-size: 16px;
    letter-spacing: 1px;
    color: var(--mist);
  }

  .band {
    position: absolute;
    left: 0; right: 0; bottom: 0;
    height: 182px;
    background: var(--teal);
  }
  .band__art {
    position: absolute;
    right: 0; bottom: 0;
    width: 230px;
    height: 182px;
    background: linear-gradient(90deg, var(--teal) 0%, var(--mist) 45%, var(--slate) 100%);
  }
  .holder {
    position: absolute;
    left: 34px; top: 28px;
    color: var(--paper);
  }
  .holder__name {
    font-family: "Exo 2", Arial, sans-serif;
    font-weight: 700;
    font-size: 24px;
    letter-spacing: 0.5px;
  }
  .holder__title { font-size: 16px; margin-top: 2px; }
  .divider {
    position: absolute;
    left: 232px; top: 30px;
    width: 1px; height: 120px;
    background: rgba(255,255,255,0.7);
  }
  .contact {
    position: absolute;
    left: 254px; top: 26px;
    color: var(--paper);
    font-size: 17px;
    line-height: 1.55;
    list-style: none;
  }
  .contact li { display: flex; align-items: center; gap: 8px; }
  .contact svg { width: 16px; height: 16px; flex: none; }
</style>
</head>
<body>
  <section class="card card--back">
    <div class="lockup">
      <div class="lockup__row">
        <span class="lockup__name">QVAR</span>
        <span class="lockup__mark"></span>
      </div>
      <div class="lockup__rule"></div>
      <div class="lockup__full">Harmonic Lattice<br>of Cognition Network</div>
    </div>
    <p class="tagline">Maximising Performance for Highly Effective People</p>
  </section>

  <section class="card card--front">
    <div class="lockup">
      <div class="lockup__row">
        <span class="lockup__name">QVAR</span>
        <span class="lockup__mark"></span>
      </div>
      <div class="lockup__rule"></div>
      <div class="lockup__full">Harmonic Lattice<br>of Cognition Network</div>
    </div>

    <div class="band">
      <div class="band__art" role="img" aria-label="Decorative bell curve graphic in teal, grey and slate"></div>
      <div class="holder">
        <div class="holder__name">MARCUS ELLERY</div>
        <div class="holder__title">Managing Director</div>
      </div>
      <div class="divider"></div>
      <ul class="contact">
        <li>48 Meridian Park Drive</li>
        <li>Suite 210, Lakewood, OH</li>
        <li>
          <svg viewBox="0 0 16 16" aria-hidden="true"><path fill="#fff" d="M3 2h3l1.5 3.5-2 1.2a9 9 0 0 0 3.8 3.8l1.2-2L14 10v3a1 1 0 0 1-1 1A11 11 0 0 1 2 3a1 1 0 0 1 1-1z"/></svg>
          31 20 448 0917
        </li>
        <li>
          <svg viewBox="0 0 16 16" aria-hidden="true"><rect x="1" y="3" width="14" height="10" fill="#fff"/><path d="M1 3l7 6 7-6" fill="none" stroke="#00a6bf" stroke-width="1.3"/></svg>
          marcus@qvarlattice.com
        </li>
      </ul>
    </div>
  </section>
</body>
</html>
```